Gas utility and appliance store needs awesome web design

Hearthline Supply is a South African based brick and mortar shop looking to improve it's on-line presence.
We cover the whole gambit or products, appliances, information, services, installations and utility related to domestic gas (in SA still considered an alternative fuel) with our most important offerings being the sale of the gas (LPG) itself in combination with high end kitchen and household gas based appliances (stoves, cookers, heaters, fireplaces etc)
Wesite needs to portray our professional (been in the market since 47), family owned (3'rd gen now) roots - it should create the impression of a market leader - and must also portray our domestic (read man in the street) focus and practical approach.
Something professional but light-hearted enough for the general public.
Design must reinforce the belief that LPG is a green,safe and affordable fuel option for domestic use

Target Market(s)

upper middle class market 25-70

Industry/Entity Type

Appliance

Requirements
Must have
• landing page
our company
sustainability
contact us page
menu bar with links to pages (shop, specific information etc)

```html
<!DOCTYPE html>
<html lang="en">
<head>
<meta charset="utf-8">
<title>Hearthline Supply</title>
<link rel="stylesheet" href="https://fonts.googleapis.com/css2?family=Arimo:wght@400;700&family=Josefin+Sans:wght@300&family=Open+Sans:wght@400&display=swap">
<style>
:root{
  --bar:#3d3d3d;--footer:#4a4a4a;--ink:#333;--muted:#666;--light:#999;
  --blue:#1a8fd6;--green:#3aa52f;--line:#d8d8d8;--card:#ccc;
}
*{box-sizing:border-box;margin:0;padding:0}
html,body{width:965px;height:1200px;overflow:hidden;background:#fff;font-family:Arimo,Arial,sans-serif;color:var(--ink)}
.page{position:relative;width:965px;height:1200px}
.topbar{position:absolute;left:0;top:0;width:965px;height:30px;background:var(--bar);font-size:7.5px;color:#eee}
.topbar span{position:absolute;top:11px}
.topbar .inquiry{left:144px;color:var(--blue)}
.search{position:absolute;left:648px;top:7px;width:173px;height:18px;background:#fff;border-radius:3px}
.search svg{position:absolute;right:5px;top:3px}
.brand{position:absolute;left:143px;top:62px;font-size:15px;font-weight:700;color:var(--blue);display:flex;align-items:center;gap:6px}
.brand i{width:12px;height:12px;border-radius:50%;background:#e03a2b;display:block}
.nav{position:absolute;left:490px;top:73px;display:flex;font-size:9px;color:#444}
.nav a{padding:6px 11px;color:inherit;text-decoration:none}
.nav a.active{background:#333;color:#fff;border-radius:2px}
.hero{position:absolute;left:145px;top:112px;width:664px;height:261px;background:linear-gradient(180deg,#3f86c9 0%,#9cc4e6 45%,#e8eef2 62%,#6aa636 78%,#4c8a25 100%)}
.hero-title{position:absolute;left:12px;top:4px;font-family:'Open Sans',sans-serif;font-size:44px;color:var(--green);line-height:1}
.hero-sub{position:absolute;left:14px;top:52px;font-family:'Open Sans',sans-serif;font-size:15px;color:#333}
.hero-badge{position:absolute;left:568px;top:14px;width:84px;height:84px;border-radius:50%;background:#8cc63f}
.hero-cta{position:absolute;left:426px;top:186px;width:232px;height:52px;background:linear-gradient(#5cbf3b,#2f8f1f);border-radius:4px;color:#fff;font-family:'Open Sans',sans-serif;font-size:17px;line-height:24px;padding:3px 22px}
.shadow{position:absolute;left:70px;top:366px;width:825px;height:40px;background:radial-gradient(ellipse at top,rgba(0,0,0,.16),transparent 70%)}
.intro{position:absolute;left:144px;top:396px;width:680px;font-family:'Josefin Sans',sans-serif;font-weight:300;font-size:23px;line-height:27px;color:#555}
.rule{position:absolute;left:143px;top:503px;width:679px;height:1px;background:var(--line)}
.label{position:absolute;top:541px;font-size:7px;font-weight:700;color:#444}
.label.right{right:143px;display:flex;align-items:center;gap:3px}
.dot{width:10px;height:10px;border-radius:50%;background:var(--blue);display:inline-block}
.card{position:absolute;top:553px;width:216px;height:220px;border:1px solid var(--card);border-radius:3px;padding:5px}
.card .media{height:101px}
.card h3{font-size:9.5px;font-weight:400;letter-spacing:.4px;margin-top:6px;line-height:13px;color:#333}
.card p{font-size:7.6px;line-height:14.3px;color:#555;margin-top:4px}
.card .meta{position:absolute;left:5px;right:5px;bottom:7px;display:flex;justify-content:space-between;font-size:7px;font-weight:700;color:#444}
.card .meta span{display:flex;align-items:center;gap:3px}
.card .meta .dot{width:9px;height:9px}
.media-brand{display:flex;align-items:center;justify-content:center;gap:6px;font-size:17px;font-weight:700;color:var(--blue)}
.feature{position:absolute;top:810px;width:160px;border-top:1px solid var(--line);padding-top:7px;font-size:8.6px;line-height:16.2px;color:#666}
.feature .icon{float:left;width:28px;height:28px;border-radius:50%;background:#3a3a3a;margin:1px 8px 0 0;display:flex;align-items:center;justify-content:center}
.crumbs{position:absolute;left:0;top:956px;width:965px;height:29px;background:#f3f3f3;border-top:1px solid #ddd;font-size:7px;color:#777}
.crumbs .path{position:absolute;left:143px;top:10px;display:flex;align-items:center;gap:5px}
.crumbs .globe{width:12px;height:12px;border-radius:50%;background:#888}
.social{position:absolute;right:143px;top:9px;display:flex;gap:4px}
.social i{width:11px;height:11px;display:block;border-radius:2px}
.footer{position:absolute;left:0;top:985px;width:965px;height:215px;background:var(--footer);color:#bbb}
.col{position:absolute;top:4px;width:116px}
.col h4{font-size:8.6px;font-weight:700;color:#eee;padding-bottom:5px;border-bottom:1px solid #666}
.col li{list-style:none;font-size:8.6px;line-height:12px;padding:4px 0 4px 7px;border-bottom:1px solid #666;position:relative}
.col li::before{content:"";position:absolute;left:1px;top:8px;border:2px solid transparent;border-left:2px solid #aaa}
.contact{width:160px}
.contact p{font-size:8.8px;line-height:16.3px;color:#eee;margin-top:4px}
.copy{position:absolute;left:0;top:1174px;width:965px;border-top:1px solid #5a5a5a;height:26px;font-size:6.6px;color:#aaa}
.copy span{position:absolute;top:10px;left:143px}
.copy .top{left:auto;right:143px}
</style>
</head>
<body>
<div class="page">
  <header class="topbar">
    <span class="inquiry">Send an inquiry</span>
    <span style="left:216px">Phone: 555 - 204771360</span>
    <span style="left:319px">info@hearthlinesupply.com</span>
    <div class="search"><svg width="12" height="12" viewBox="0 0 12 12"><circle cx="5" cy="5" r="3.5" fill="none" stroke="#222" stroke-width="1.6"/><line x1="7.5" y1="7.5" x2="11" y2="11" stroke="#222" stroke-width="1.8"/></svg></div>
  </header>

  <div class="brand"><i></i>Hearthline Supply</div>
  <nav class="nav">
    <a class="active">Home</a><a>Our Company</a><a>Sustainability</a><a>Products</a><a>Contact</a>
  </nav>

  <div class="shadow"></div>
  <section class="hero" role="img" aria-label="Photo of a happy child running across a green lawn under a blue cloudy sky with city towers and a leafy globe">
    <div class="hero-title">LPG</div>
    <div class="hero-sub">Cleaner, Safer &amp; Environment Friendly</div>
    <div class="hero-badge" role="img" aria-label="Eco friendly badge"></div>
    <div class="hero-cta">Find out more about our LPG Products</div>
  </section>

  <p class="intro">Hello! We are the Third Generation of Hearthline Supply. Over 47 years of experience in the LP Gas industry ensures that you are in good hands at Hearthline Supply.... Afterall we make GAS Hot!</p>
  <div class="rule"></div>

  <div class="label" style="left:143px">OUR COMPANY:</div>
  <div class="label right">SEND AN INQUIRY <span class="dot"></span></div>

  <article class="card" style="left:143px">
    <div class="media media-brand">Hearthline Supply</div>
    <h3>OVER 65 YEARS OF MAKING LIVES BETTER</h3>
    <p>Lorem ipsum dolor sit amet, consectetur adipisicing elit, sed do eiusmod tempor incididunt ut labolore magna aliqua. Ut enim ad minim veniam.</p>
    <div class="meta"><span><i class="dot"></i>Web Design, Webworks</span><span>Dec. 03. 09 <i class="dot"></i></span></div>
  </article>
  <article class="card" style="left:374px">
    <div class="media" role="img" aria-label="Photo of a gas cylinder, kettle barbecue and gas stove on grass" style="background:linear-gradient(90deg,#9bc94a,#dfe9c8 60%,#f2f2f2)"></div>
    <h3>OUR PRODUCTS - YOUR TOTAL GAS SOLUTION</h3>
    <p>Lorem ipsum dolor sit amet, consectetur adipisicing elit, sed do eiusmod tempor incididunt ut labolore magna aliqua. Ut enim ad minim veniam.</p>
    <div class="meta"><span><i class="dot"></i>Web Design, Webworks</span><span>Dec. 03. 09 <i class="dot"></i></span></div>
  </article>
  <article class="card" style="left:605px">
    <div class="media" role="img" aria-label="Photo of a smiling baby holding a daisy in green grass" style="background:linear-gradient(90deg,#6fa83a,#b9d68a 55%,#e9d6c2)"></div>
    <h3>LPG - A GREENER, SAFER &amp; AFFORDABLE FUEL</h3>
    <p>Lorem ipsum dolor sit amet, consectetur adipisicing elit, sed do eiusmod tempor incididunt ut labolore magna aliqua. Ut enim ad minim veniam.</p>
    <div class="meta"><span><i class="dot"></i>Web Design, Webworks</span><span>Dec. 03. 09 <i class="dot"></i></span></div>
  </article>

  <div class="feature" style="left:143px"><span class="icon"><svg width="16" height="16" viewBox="0 0 16 16"><path d="M8 1l2 5h5l-4 3 1.6 5L8 11l-4.6 3L5 9 1 6h5z" fill="#fff"/></svg></span>Lorem ipsum dolor sit amet, consectetur adipisicing elit, sed do eiusmod tempor incididunt ut labore et dolore magna aliqua. Ut enim ad minim veniam, quis nostrud exercitation ullamco laboris nisi ut aliquip ex ea commodo conse.</div>
  <div class="feature" style="left:317px"><span class="icon"><svg width="16" height="12" viewBox="0 0 16 12"><rect x="1" y="1" width="14" height="10" rx="1" fill="#fff"/><path d="M1 1l7 6 7-6" fill="none" stroke="#3a3a3a" stroke-width="1.4"/></svg></span>Consectetur adipisicing elit, sed do eiusmod tempor incididunt ut labore et dolore im veniam.<br>quis nostrud exercitation ullamco laboris nisi ut aliquip ex ea commodo cem ipsum dolor sit amet.</div>
  <div class="feature" style="left:490px"><span class="icon"><svg width="14" height="14" viewBox="0 0 14 14"><rect x="1" y="7" width="3" height="6" fill="#fff"/><rect x="5.5" y="4" width="3" height="9" fill="#fff"/><rect x="10" y="1" width="3" height="12" fill="#fff"/></svg></span>Lorem ipsum dolor sit amet, consectetur adipisicing elit, sed do eiusmod tempor incididunt ut labore et dolore magna aliqua. Ut enim ad minim veniam, quis nostrud exercitation ullamco laboris nisi ut aliquip ex ea commodo conse.</div>
  <div class="feature" style="left:663px"><span class="icon"><svg width="16" height="14" viewBox="0 0 16 14"><rect x="1" y="1" width="14" height="9" rx="1" fill="#fff"/><rect x="6" y="10" width="4" height="2" fill="#fff"/><rect x="4" y="12" width="8" height="1.5" fill="#fff"/></svg></span>Ut enim ad minim veniam, quis nostrud exercitation ullamco laboris nisi ut aliquip ex ea commodo conse. Lorem ipsum dolor sit amet.<br>Sed do eiusmod tempor incididunt ut labore et dolore magna aliqua.</div>

  <div class="crumbs">
    <div class="path"><i class="globe"></i>Home &rsaquo; About &rsaquo; <span style="color:#444">Over 65 years of making lives better</span></div>
    <div class="social"><i style="background:#f08a24"></i><i style="background:#3b5b98"></i><i style="background:#4aa8e0"></i><i style="background:#e33b7a"></i><i style="background:#23a6e0"></i></div>
  </div>

  <footer class="footer">
    <div class="col" style="left:143px"><h4>Latest News</h4><ul><li>Our New Page is online</li><li>Example</li><li>Example</li><li>Example</li></ul></div>
    <div class="col" style="left:273px"><h4>Pages</h4><ul><li>Home</li><li>About</li><li>Company Info</li><li>Sustainability</li><li>Products</li><li>Contact Us</li></ul></div>
    <div class="col" style="left:403px"><h4>Key Products</h4><ul><li>LPG</li><li>BBQ</li><li>Build-in Hobs</li><li>Build-in Ovans</li><li>Coffee Machine</li><li>Extractor Hoods</li><li>Heaters</li></ul></div>
    <div class="col" style="left:533px"><h4>Miscellaneous</h4><ul><li>Subscribe for News Letter</li><li>Terms of Service</li><li>Site Map</li></ul></div>
    <div class="col contact" style="left:663px"><h4>Contact Information</h4>
      <p>P.O. Box 41290<br>Rietvlei Park 0152<br>South Africa<br>Ph: 00 - 000- 00000<br>Fax: 00 - 000 - 00000</p>
      <p style="margin-top:9px">We're available from 9 AM- 5 PM.</p>
    </div>
  </footer>
  <div class="copy"><span>All content Copyright &copy; 2010 Brightfold, Inc</span><span class="top">top &#8963;</span></div>
</div>
</body>
</html>
```